Party Decoration Set Designs - Rose Gold theme - more example images just added

We are looking for a set of designs for a set of party decorations. It’s a Rose Gold colored theme. I have attached some photos of some glittery rose gold items that I think would go good with the theme. There are also some photos of full sets of decorations in other colors schemes to give an idea of what we are looking for.

We would like to have designs for the items below:

1- Happy Birthday Flag Banner- looking for something unique. Size- 5”X7” WXL

2- hanging swirl cards ( photo examples attached) 4”X6” approx. can be different sizes and shapes.

3- centerpiece designs- photo examples attached. Middle
Piece that’s says Happy Birthday should be 5”X 7” and the smaller surrounding pieces 3X5

4 - round candy stickers and candy wrappers. Examples below. .75 inch

The photos below are of products currently sold. We would like to be very similar to these but just a little different to make our own. And then to have a Happy Birthday banner created to match the theme.

Some of these example photos below are from different themes and colors But I included them because they are the complete set we want to create. First we will do a generic “Happy Birthday” Set with rose gold glitter theme and then later we will add the Sweet 16 birthday theme as well and 40th, 50th etc.

On the centerpieces where the example photos how a large “40”, we would like this to be a larger “Happy Birthday” design. Then surrounded by some smaller designs.
I look forward to receiving your ideas

Target Market(s)

Anyone looking for birthday Peru decorations for a female.

Font styles to use
Other font styles liked:
• Open to designer suggestion

Requirements
Must have
• Happy Birthday Banner, Hanging swirl cards, centerpiece cards, cake topper
Nice to have
• We are certainly open to any creative ideas.
Should not have
• I just now added some example images of a very good set of exactly what we want but its in a different theme. This is a black gold set and our requested design is more feminine and Rose Gold color

```html
<!DOCTYPE html>
<html lang="en">
<head>
<meta charset="utf-8">
<title>Rose Gold Birthday Party Set</title>
<link rel="stylesheet" href="https://fonts.googleapis.com/css2?family=Great+Vibes&family=Nunito+Sans:wght@800&family=Righteous&display=swap">
<style>
  :root {
    --navy: #241e3a;
    --rose: #c47d7a;
    --rose-deep: #a9605e;
    --rose-light: #e9c2bb;
    --leaf-bg: #ecd9da;
    --paper: #ffffff;
    --white: #ffffff;
  }
  * { margin: 0; padding: 0; box-sizing: border-box; }
  html, body { width: 1200px; height: 848px; overflow: hidden; background: var(--paper); }
  .sheet { position: relative; width: 1200px; height: 848px; overflow: hidden; }
  .section-title {
    position: absolute;
    font-family: "Nunito Sans", Arial, sans-serif;
    font-weight: 800;
    font-size: 26px;
    line-height: 1.15;
    color: #000;
  }
  .piece { position: absolute; display: block; overflow: hidden; }
  .swirl-card { overflow: visible; }
  .backdrop-leaf { position: absolute; left: 0; top: 0; }
  .script { font-family: "Great Vibes", cursive; }
  .display { font-family: "Righteous", sans-serif; }
</style>
</head>
<body>
<main class="sheet">

  <svg class="defs" width="0" height="0" aria-hidden="true" style="position:absolute">
    <defs>
      <clipPath id="flag-shape" clipPathUnits="userSpaceOnUse">
        <path d="M0 0H154V215L77 173L0 215Z"/>
      </clipPath>
      <clipPath id="flag-inner" clipPathUnits="userSpaceOnUse">
        <path d="M4 5H150V205L77 166L4 205Z"/>
      </clipPath>
      <clipPath id="hex-shape" clipPathUnits="userSpaceOnUse">
        <path d="M12 188L63 93H166L222 188L179 286H63Z"/>
      </clipPath>
      <linearGradient id="glitter" x1="0" y1="0" x2="1" y2="1">
        <stop offset="0" stop-color="#f3d2c9"/>
        <stop offset="0.45" stop-color="#d3918a"/>
        <stop offset="0.7" stop-color="#b66a64"/>
        <stop offset="1" stop-color="#e7b7ae"/>
      </linearGradient>
      <linearGradient id="leaf-wash" x1="0" y1="0" x2="1" y2="1">
        <stop offset="0" stop-color="#c47d7a" stop-opacity="0.95"/>
        <stop offset="0.6" stop-color="#c47d7a" stop-opacity="0.55"/>
        <stop offset="1" stop-color="#c47d7a" stop-opacity="0.15"/>
      </linearGradient>
      <linearGradient id="leaf-wash-soft" x1="0" y1="0" x2="1" y2="1">
        <stop offset="0" stop-color="#c47d7a" stop-opacity="0.55"/>
        <stop offset="1" stop-color="#c47d7a" stop-opacity="0.1"/>
      </linearGradient>
      <linearGradient id="rose-satin" x1="0" y1="0" x2="1" y2="1">
        <stop offset="0" stop-color="#e4aaa4"/>
        <stop offset="0.5" stop-color="#d28e89"/>
        <stop offset="1" stop-color="#b86a67"/>
      </linearGradient>
      <radialGradient id="splash" cx="0.5" cy="0.5" r="0.5">
        <stop offset="0" stop-color="#eab9ae"/>
        <stop offset="0.7" stop-color="#d2928a" stop-opacity="0.9"/>
        <stop offset="1" stop-color="#d2928a" stop-opacity="0"/>
      </radialGradient>
      <radialGradient id="backdrop" cx="0.5" cy="0.5" r="0.5">
        <stop offset="0" stop-color="#ecd9da" stop-opacity="0.9"/>
        <stop offset="1" stop-color="#ecd9da" stop-opacity="0"/>
      </radialGradient>
    </defs>
  </svg>

  <svg class="backdrop-leaf" width="1200" height="848" viewBox="0 0 1200 848" role="img" aria-label="Large faint palm leaf decoration">
    <ellipse cx="930" cy="400" rx="520" ry="360" fill="url(#backdrop)"/>
  </svg>

  <!-- Centerpiece -->
  <h2 class="section-title" style="left:30px; top:28px;">Centerpiece</h2>

  <svg class="piece centerpiece-card" style="left:27px; top:81px;" width="154" height="215" viewBox="0 0 154 215">
    <path d="M0 0H154V215L77 173L0 215Z" fill="var(--navy)"/>
    <path d="M0 0H154V215L77 173L0 215Z" fill="url(#leaf-wash)" role="img" aria-label="Rose palm leaf pattern"/>
    <g clip-path="url(#flag-shape)">
      <text class="script" x="76" y="82" text-anchor="middle" font-size="46" fill="var(--white)" transform="rotate(-6 76 82)">Happy</text>
      <text class="script" x="78" y="138" text-anchor="middle" font-size="42" fill="var(--white)" transform="rotate(-6 78 138)">Birthday</text>
    </g>
  </svg>

  <svg class="piece centerpiece-card" style="left:204px; top:81px;" width="154" height="215" viewBox="0 0 154 215">
    <path d="M0 0H154V215L77 173L0 215Z" fill="var(--navy)"/>
    <path d="M0 0H154V215L77 173L0 215Z" fill="url(#leaf-wash)" role="img" aria-label="Rose palm leaf pattern"/>
    <g clip-path="url(#flag-shape)">
      <text class="script" x="80" y="82" text-anchor="middle" font-size="38" fill="var(--white)" transform="rotate(-5 80 82)">Happy</text>
      <text class="script" x="80" y="120" text-anchor="middle" font-size="36" fill="var(--white)" transform="rotate(-5 80 120)">Birthday</text>
    </g>
  </svg>

  <svg class="piece centerpiece-card" style="left:374px; top:81px;" width="154" height="215" viewBox="0 0 154 215">
    <path d="M0 0H154V215L77 173L0 215Z" fill="var(--navy)"/>
    <path d="M0 0H154V215L77 173L0 215Z" fill="url(#glitter)" opacity="0.8" role="img" aria-label="Rose gold glitter palm leaf pattern"/>
    <g clip-path="url(#flag-shape)">
      <text class="script" x="80" y="82" text-anchor="middle" font-size="38" fill="var(--white)" transform="rotate(-5 80 82)">Happy</text>
      <text class="script" x="80" y="120" text-anchor="middle" font-size="36" fill="var(--white)" transform="rotate(-5 80 120)">Birthday</text>
    </g>
  </svg>

  <!-- Swirl -->
  <h2 class="section-title" style="left:639px; top:28px;">Swirl</h2>

  <svg class="piece swirl-card" style="left:650px; top:0;" width="220" height="300" viewBox="0 0 220 300">
    <path d="M115 0C95 20 130 35 100 52C80 64 118 70 110 86" fill="none" stroke="var(--rose)" stroke-width="9" stroke-linecap="round"/>
    <circle cx="110" cy="188" r="107" fill="url(#glitter)"/>
    <circle cx="110" cy="188" r="100" fill="var(--navy)"/>
    <path d="M10 188A100 100 0 0 1 110 88L210 188A100 100 0 0 1 110 288Z" fill="url(#leaf-wash-soft)" role="img" aria-label="Rose palm leaf pattern"/>
    <text class="script" x="105" y="165" text-anchor="middle" font-size="56" fill="url(#glitter)" stroke="#8a4e4b" stroke-width="0.6" transform="rotate(-8 105 165)">Happy</text>
    <text class="script" x="113" y="236" text-anchor="middle" font-size="50" fill="url(#glitter)" stroke="#8a4e4b" stroke-width="0.6" transform="rotate(-8 113 236)">Birthday</text>
  </svg>

  <svg class="piece swirl-card" style="left:880px; top:0;" width="236" height="300" viewBox="0 0 236 300">
    <path d="M100 0C80 20 115 35 86 52C66 64 104 70 96 86" fill="none" stroke="var(--rose)" stroke-width="9" stroke-linecap="round"/>
    <path d="M2 188L57 83H172L234 188L185 296H57Z" fill="var(--navy)"/>
    <ellipse cx="125" cy="182" rx="95" ry="78" fill="url(#splash)" clip-path="url(#hex-shape)" role="img" aria-label="Rose gold glitter splash"/>
    <path d="M12 188L63 93H166L222 188L179 286H63Z" fill="none" stroke="var(--rose)" stroke-width="3"/>
    <path d="M150 100l5 13 14 1-11 8 4 14-12-8-12 8 4-14-11-8 14-1z" fill="none" stroke="var(--white)" stroke-width="1.6"/>
    <text class="display" x="125" y="182" text-anchor="middle" font-size="38" fill="var(--white)">PARTY</text>
    <text class="display" x="125" y="222" text-anchor="middle" font-size="38" fill="var(--white)">TIME!</text>
  </svg>

  <!-- Banner -->
  <h2 class="section-title" style="left:30px; top:340px;">Banner</h2>

  <svg class="piece banner-flag" style="left:27px; top:377px;" width="154" height="215" viewBox="0 0 154 215">
    <path d="M0 0H154V215L77 173L0 215Z" fill="var(--navy)"/>
    <path d="M4 5H150V205L77 166L4 205Z" fill="none" stroke="var(--rose)" stroke-width="3"/>
    <text class="script" x="77" y="122" text-anchor="middle" font-size="86" fill="url(#glitter)" clip-path="url(#flag-inner)">H</text>
  </svg>
  <svg class="piece banner-flag" style="left:196px; top:377px;" width="154" height="215" viewBox="0 0 154 215">
    <path d="M0 0H154V215L77 173L0 215Z" fill="var(--navy)"/>
    <path d="M4 5H150V205L77 166L4 205Z" fill="none" stroke="var(--rose)" stroke-width="3"/>
    <text class="script" x="77" y="122" text-anchor="middle" font-size="86" fill="url(#glitter)" clip-path="url(#flag-inner)">A</text>
  </svg>
  <svg class="piece banner-flag" style="left:363px; top:377px;" width="154" height="215" viewBox="0 0 154 215">
    <path d="M0 0H154V215L77 173L0 215Z" fill="var(--navy)"/>
    <path d="M4 5H150V205L77 166L4 205Z" fill="none" stroke="var(--rose)" stroke-width="3"/>
    <text class="script" x="77" y="122" text-anchor="middle" font-size="86" fill="url(#glitter)" clip-path="url(#flag-inner)">P</text>
  </svg>
  <svg class="piece banner-flag" style="left:531px; top:377px;" width="154" height="215" viewBox="0 0 154 215">
    <path d="M0 0H154V215L77 173L0 215Z" fill="var(--navy)"/>
    <path d="M4 5H150V205L77 166L4 205Z" fill="none" stroke="var(--rose)" stroke-width="3"/>
    <text class="script" x="77" y="122" text-anchor="middle" font-size="86" fill="url(#glitter)" clip-path="url(#flag-inner)">P</text>
  </svg>
  <svg class="piece banner-flag" style="left:705px; top:377px;" width="154" height="215" viewBox="0 0 154 215">
    <path d="M0 0H154V215L77 173L0 215Z" fill="var(--navy)"/>
    <path d="M4 5H150V205L77 166L4 205Z" fill="none" stroke="var(--rose)" stroke-width="3"/>
    <text class="script" x="77" y="118" text-anchor="middle" font-size="86" fill="url(#glitter)" clip-path="url(#flag-inner)">Y</text>
  </svg>

  <svg class="piece banner-flag" style="left:27px; top:613px;" width="154" height="215" viewBox="0 0 154 215">
    <path d="M0 0H154V215L77 173L0 215Z" fill="var(--navy)"/>
    <path d="M4 5H150V205L77 166L4 205Z" fill="url(#leaf-wash-soft)" role="img" aria-label="Rose palm leaf pattern"/>
    <path d="M4 5H150V205L77 166L4 205Z" fill="none" stroke="var(--rose)" stroke-width="3"/>
    <text class="script" x="77" y="130" text-anchor="middle" font-size="92" fill="url(#glitter)" stroke="var(--white)" stroke-width="0.8" clip-path="url(#flag-inner)">H</text>
  </svg>
  <svg class="piece banner-flag" style="left:196px; top:613px;" width="154" height="215" viewBox="0 0 154 215">
    <path d="M0 0H154V215L77 173L0 215Z" fill="var(--navy)"/>
    <ellipse cx="77" cy="98" rx="80" ry="72" fill="url(#splash)" clip-path="url(#flag-inner)" role="img" aria-label="Rose gold glitter splash"/>
    <path d="M4 5H150V205L77 166L4 205Z" fill="none" stroke="var(--rose)" stroke-width="3"/>
    <text class="display" x="77" y="126" text-anchor="middle" font-size="76" fill="var(--white)">H</text>
  </svg>

  <!-- Round Sticker -->
  <h2 class="section-title" style="left:535px; top:612px;">Round<br>Sticker</h2>

  <svg class="piece round-sticker" style="left:623px; top:614px;" width="202" height="202" viewBox="0 0 202 202">
    <circle cx="101" cy="101" r="101" fill="var(--navy)"/>
    <path d="M0 101A101 101 0 0 1 172 30L30 172A101 101 0 0 1 0 101Z" fill="url(#rose-satin)"/>
    <text class="display" x="101" y="92" text-anchor="middle" font-size="34" fill="url(#glitter)" stroke="#9a5a57" stroke-width="0.6">HAPPY</text>
    <text class="display" x="101" y="128" text-anchor="middle" font-size="34" fill="url(#glitter)" stroke="#9a5a57" stroke-width="0.6">BIRTHDAY</text>
  </svg>

  <svg class="piece round-sticker" style="left:857px; top:614px;" width="202" height="202" viewBox="0 0 202 202">
    <circle cx="101" cy="101" r="101" fill="url(#rose-satin)"/>
    <circle cx="101" cy="101" r="101" fill="url(#leaf-wash-soft)" opacity="0.6" role="img" aria-label="Soft palm leaf pattern"/>
    <text class="display" x="101" y="92" text-anchor="middle" font-size="34" fill="var(--navy)" stroke="#e8b8b0" stroke-width="0.8">HAPPY</text>
    <text class="display" x="101" y="128" text-anchor="middle" font-size="34" fill="var(--navy)" stroke="#e8b8b0" stroke-width="0.8">BIRTHDAY</text>
  </svg>

</main>
</body>
</html>
```